Identity Package (Logo, Website)

We need a logo and website design for a new company.
The new company is a voicemail transcription service provider. It's name is KL9BQZ.io
It will be very transactional. We like the "bootstrap" look and feel, and will be using a developer familiar with bootstrap. Here are the kinds of webpages we like :
https://www.lumenvane.io
http://www.quorbil.com/
http://www.plenivo.com/
There will only be 5 pages, as follows :
1- Homepage
2- Voicemail Transcription for Individuals
3- Voicemail Transcription for Companies
4- Wholesale Voicemail Transcription for Service Providers/Enterprises
5- Contact us
As far as the logo is concerned, we'd like to have just stylized text. It should be done in such a way as to make it easy to see the different elements of the name, which are KL, 2, and BQZ.
Reason: I have received a number of designs, but the designs are mostly from the same few designers (not that much variety in designers). I'd like a few more to compare if possible, so I thought I would keep this open until Monday to give more designers the opportunity to submit over the weekend. Thanks!

```html
<!DOCTYPE html>
<html lang="en">
<head>
<meta charset="utf-8">
<title>KL9BQZ.io – Voicemail to Text Services</title>
<link rel="stylesheet" href="https://fonts.googleapis.com/css2?family=Open+Sans:wght@400;600;700&display=swap">
<style>
:root{
  --green:#8cc63e;
  --green-dark:#79b02f;
  --ink:#333;
  --muted:#777;
  --line:#dcdcdc;
  --pale:#f1f2f2;
  --panel:#e9edee;
  --dark:#333;
  --darker:#262626;
  --white:#fff;
}
*{box-sizing:border-box;margin:0;padding:0}
html,body{width:1200px;height:2581px;overflow:hidden}
body{font-family:"Open Sans",Arial,sans-serif;color:var(--ink);background:var(--white);font-size:13px}
.wrap{width:870px;margin:0 auto;position:relative;height:100%}
section,header,footer{position:relative;overflow:hidden}

/* top bar */
.topbar{height:26px;background:#f5f5f5;border-bottom:1px solid #e6e6e6;font-size:10px;color:#888}
.topbar .wrap{display:flex;justify-content:space-between;align-items:center}
.social{display:flex;gap:18px}
.social span{width:9px;height:9px;border-radius:50%;background:#aaa;display:block}

/* nav */
.masthead{height:88px;border-bottom:1px solid #e4e4e4}
.masthead .wrap{display:flex;justify-content:space-between;align-items:center}
.brand{font-size:34px;font-weight:700;color:#3a3a3a;letter-spacing:-1px}
.menu{display:flex;gap:38px;list-style:none;font-size:11.5px;font-weight:600;height:100%;align-items:center}
.menu li{position:relative;height:100%;display:flex;align-items:center}
.menu .active{color:var(--green)}
.menu .active::after{content:"";position:absolute;left:-10px;right:-10px;bottom:0;height:3px;background:var(--green)}

/* hero */
.hero{height:397px;background:radial-gradient(circle at 20% 40%,#c9d98a 0,#7aa644 25%,transparent 50%),radial-gradient(circle at 45% 25%,#c6554b 0,transparent 22%),linear-gradient(120deg,#6a9a3c,#4d7a30 40%,#3d6a2c 70%,#5f8f3a)}
.hero-art{position:absolute;left:52px;top:40px;width:310px;height:270px;border-radius:8px;background:rgba(255,255,255,.12)}
.hero-copy{position:absolute;left:658px;top:67px;width:420px;color:var(--white)}
.hero-title{display:inline-block;background:rgba(25,25,25,.85);padding:9px 14px;font-size:24px;font-weight:700;letter-spacing:.5px}
.hero-sub{margin-top:20px;font-size:24px;font-weight:600;color:#a5de55;line-height:1.3}
.hero-rule{margin:22px 0 10px;height:1px;background:rgba(255,255,255,.6)}
.hero-note{font-size:10.5px;letter-spacing:.3px}
.btn{display:inline-block;background:var(--green);color:var(--white);font-weight:700;font-size:12px;padding:10px 22px;border-radius:2px}
.hero .btn{margin-top:42px}
.arrow{position:absolute;top:180px;width:28px;height:34px;background:#1c1c1c;display:flex;align-items:center;justify-content:center}
.arrow.l{left:0}.arrow.r{right:0}

/* features */
.features{height:302px}
.feature-grid{display:grid;grid-template-columns:repeat(4,1fr);gap:20px;padding-top:66px;text-align:center}
.feature-icon{width:66px;height:66px;border-radius:50%;background:var(--green);margin:0 auto 18px;display:flex;align-items:center;justify-content:center}
.feature h3{font-size:14px;font-weight:700;margin-bottom:8px}
.feature p{font-size:11.5px;color:var(--muted);line-height:1.5}

/* possibilities */
.possibilities{height:426px;background:var(--pale);border-top:1px solid var(--line);border-bottom:1px solid var(--line)}
.section-head{text-align:center;padding-top:30px}
.section-head h2{font-size:19px;font-weight:400}
.section-head h2 b{font-weight:700}
.section-head p{font-size:11.5px;color:#555;line-height:1.6;margin-top:6px}
.pager{display:flex;gap:4px;justify-content:center;margin-top:16px;position:relative;z-index:1}
.pager span{width:22px;height:22px;background:#c8c8c8;display:flex;align-items:center;justify-content:center}
.pager span.on{background:#555}
.gallery-rule{height:1px;background:var(--line);margin-top:-11px;position:relative;z-index:0}
.gallery{display:grid;grid-template-columns:repeat(4,200px);gap:23px;margin-top:24px}
.photo{height:207px}

/* why + testimonials */
.split{height:413px}
.split .wrap{display:flex;justify-content:space-between;padding-top:60px}
.col-left{width:418px}.col-right{width:410px}
.col-title{font-size:14px;font-weight:700;padding-bottom:12px;border-bottom:1px solid var(--line);display:flex;justify-content:space-between;align-items:center}
.accordion{margin-top:20px}
.acc-open{border:3px solid #e2e2e2;background:var(--white);padding:12px 16px;height:124px}
.acc-open h4{color:var(--green);font-size:12.5px;font-weight:700;display:flex;justify-content:space-between;padding-bottom:10px;border-bottom:1px solid #e6e6e6}
.acc-open p{font-size:11.5px;color:#555;line-height:1.55;margin-top:10px}
.acc-row{height:52px;background:#e7e8e8;margin-top:3px;display:flex;justify-content:space-between;align-items:center;padding:0 16px;font-size:12.5px;font-weight:700}
.sign{font-size:18px;color:#888;font-weight:400}
.mini-pager{display:flex;gap:4px}
.mini-pager span{width:22px;height:22px;background:#c8c8c8;display:flex;align-items:center;justify-content:center}
.mini-pager span.on{background:#555}
.quote{margin-top:20px;background:var(--panel);height:180px;position:relative;padding:22px 22px 0 190px;font-size:12px;color:#555;line-height:1.6}
.quote::after{content:"";position:absolute;left:60px;bottom:-18px;border:18px solid transparent;border-top-color:var(--panel);border-bottom:0}
.avatar{position:absolute;left:48px;top:22px;width:96px;height:96px;border-radius:50%;background:linear-gradient(150deg,#7a4f3a,#c79a80);border:4px solid var(--white)}
.who{position:absolute;left:36px;top:126px;text-align:center;width:120px;font-size:11px;color:#666;line-height:1.3}
.who small{display:block;font-size:9px;color:#999}

/* cta */
.cta{height:245px;background:linear-gradient(90deg,#6a5a4a,#b9a58b 30%,#d8c8a4 55%,#c5c0a0 75%,#9aa068)}
.cta-box{position:absolute;left:173px;top:77px;width:872px;height:91px;background:rgba(255,255,255,.78);display:flex;justify-content:space-between;align-items:center;padding:0 36px}
.cta-box h2{font-size:24px;font-weight:700;color:#2e2e2e}

/* partners */
.partners{height:284px}
.partners h3{font-size:15px;font-weight:700;padding-top:44px;padding-bottom:10px;border-bottom:1px solid var(--line)}
.partner-row{display:grid;grid-template-columns:repeat(5,1fr);border:1px solid var(--line);margin-top:28px;height:88px}
.partner{border-right:1px solid var(--line);display:flex;align-items:center;justify-content:center}
.partner:last-child{border-right:0}
.partner span{width:110px;height:34px;background:#d6d6d6;border-radius:3px}

/* tweet bar */
.tweetbar{height:44px;background:var(--green);color:var(--white);font-size:10.5px}
.tweetbar .wrap{display:flex;align-items:center;gap:12px}
.tweetbar .dot{width:12px;height:12px;border-radius:50%;background:var(--white)}
.bullets{margin-left:auto;display:flex;gap:8px}
.bullets span{width:8px;height:8px;border-radius:50%;background:#3e5a1b}
.bullets span.on{background:var(--white)}

/* footer */
.footer{height:317px;background:var(--dark);color:#bbb;font-size:11px}
.footer .wrap{display:grid;grid-template-columns:230px 227px 224px 1fr;padding-top:42px}
.footer .brand{font-size:30px;color:#e5e5e5}
.footer p{line-height:1.6;margin-top:8px;width:200px}
.footer h4{color:var(--white);font-size:12.5px;font-weight:700;margin:14px 0 14px}
.posts{list-style:none}
.posts li{margin-bottom:9px}
.posts li::before{content:"›";color:#999;margin-right:8px}
.stream{display:grid;grid-template-columns:repeat(3,44px);gap:8px}
.stream span{height:44px;background:linear-gradient(135deg,#3f6f96,#a7c3d6)}
.stream span:nth-child(3n+2){background:linear-gradient(135deg,#2c2c3c,#6a7a8a)}
.stream span:nth-child(4n){background:linear-gradient(135deg,#5e7f9c,#e1e6ea)}
.tags{display:flex;flex-wrap:wrap;gap:6px;width:190px}
.tags span{background:#444;color:#ddd;padding:5px 8px;font-size:10px}
.copyright{height:39px;background:var(--darker);color:#999;font-size:10px}
.copyright .wrap{display:flex;align-items:center}
</style>
</head>
<body>

<header class="topbar">
  <div class="wrap">
    <span>Call Us: (310) 555-0148 &nbsp;·&nbsp; Mail: hello@kl9bqz.io</span>
    <div class="social"><span></span><span></span><span></span><span></span><span></span></div>
  </div>
</header>

<header class="masthead">
  <div class="wrap">
    <div class="brand">KL9BQZ.io</div>
    <ul class="menu">
      <li class="active">HOME</li>
      <li>FOR INDIVIDUALS</li>
      <li>FOR COMPANIES</li>
      <li>FOR WHOLESELLERS</li>
      <li>CONTACT</li>
    </ul>
  </div>
</header>

<section class="hero">
  <div class="hero-art" role="img" aria-label="Illustration of a user linked to message, mail and phone icons"></div>
  <div class="hero-copy">
    <div class="hero-title">VOICEMAIL TO TEXT SERVICES</div>
    <div class="hero-sub">Read Your Voicemails Anywhere, Anytime on Your Mobile Phone.</div>
    <div class="hero-rule"></div>
    <div class="hero-note">TEXT DELIVERY ENSURES YOU GET THE MESSAGE ANYWHERE AT ANY TIME</div>
    <span class="btn">PURCHASE NOW</span>
  </div>
  <div class="arrow l"><svg width="10" height="14"><path d="M8 1 2 7l6 6" stroke="#fff" stroke-width="2" fill="none"/></svg></div>
  <div class="arrow r"><svg width="10" height="14"><path d="M2 1l6 6-6 6" stroke="#fff" stroke-width="2" fill="none"/></svg></div>
</section>

<section class="features">
  <div class="wrap feature-grid">
    <div class="feature">
      <div class="feature-icon"><svg width="30" height="30" viewBox="0 0 30 30"><path d="M4 13h5v13H4zM11 26V13l5-9c2 0 3 1 3 3l-1 5h7c1.5 0 2.5 1.3 2 3l-3 9c-.4 1.3-1.3 2-2.5 2z" fill="#fff"/></svg></div>
      <h3>AWESOME SUPPORT</h3>
      <p>Neque porro quisquam est, qui dolorem ipsum quia dolor sit consectetur, adipisci.</p>
    </div>
    <div class="feature">
      <div class="feature-icon"><svg width="30" height="30" viewBox="0 0 30 30"><path d="M4 4h22v16H13l-6 6v-6H4z" fill="#fff"/><path d="M9 10h12M9 14h8" stroke="#8cc63e" stroke-width="2"/></svg></div>
      <h3>VOICE BIOMETRICS</h3>
      <p>Neque porro quisquam est, qui dolorem ipsum quia dolor sit consectetur, adipisci.</p>
    </div>
    <div class="feature">
      <div class="feature-icon"><svg width="30" height="30" viewBox="0 0 30 30"><rect x="4" y="6" width="18" height="20" fill="none" stroke="#fff" stroke-width="2.5"/><path d="M12 18l12-12 3 3-12 12-4 1z" fill="#fff"/></svg></div>
      <h3>TRANSCRIPTION</h3>
      <p>Neque porro quisquam est, qui dolorem ipsum quia dolor sit consectetur, adipisci.</p>
    </div>
    <div class="feature">
      <div class="feature-icon"><svg width="30" height="30" viewBox="0 0 30 30"><path d="M15 3h12v12L14 28 2 16z" fill="#fff"/><circle cx="21" cy="9" r="2.5" fill="#8cc63e"/></svg></div>
      <h3>AFFORDABLE PLANS</h3>
      <p>Neque porro quisquam est, qui dolorem ipsum quia dolor sit consectetur, adipisci.</p>
    </div>
  </div>
</section>

<section class="possibilities">
  <div class="wrap">
    <div class="section-head">
      <h2>YOUR MOBILE LIFE, <b>COUNTLESS POSSIBILITIES</b></h2>
      <p>Download mobile apps for life, work and play. Powerful transcription. More control. More accurate. Faster.<br>Professionally customer service with robust ideas.</p>
    </div>
    <div class="pager">
      <span><svg width="8" height="10"><path d="M6 1 2 5l4 4" stroke="#fff" stroke-width="2" fill="none"/></svg></span>
      <span class="on"><svg width="8" height="10"><path d="M2 1l4 4-4 4" stroke="#fff" stroke-width="2" fill="none"/></svg></span>
    </div>
    <div class="gallery-rule"></div>
    <div class="gallery">
      <div class="photo" role="img" aria-label="Photo of a doctor using a mobile phone" style="background:linear-gradient(160deg,#e9eef0,#b9c6cc)"></div>
      <div class="photo" role="img" aria-label="Photo of a hand holding a smartphone" style="background:linear-gradient(160deg,#3a3a3a,#7a7a6a)"></div>
      <div class="photo" role="img" aria-label="Photo of business people in a meeting" style="background:linear-gradient(160deg,#c8cdd0,#5a5f66)"></div>
      <div class="photo" role="img" aria-label="Photo of a businessman on a phone call" style="background:linear-gradient(160deg,#dfe3e0,#8c9a8a)"></div>
    </div>
  </div>
</section>

<section class="split">
  <div class="wrap">
    <div class="col-left">
      <div class="col-title">WHY CHOOSE US</div>
      <div class="accordion">
        <div class="acc-open">
          <h4>Professional UI <span class="sign" style="color:#555">−</span></h4>
          <p>Completely synergize resource sucking relationships via premier niche markets. Professionally customer service with robust ideas.</p>
        </div>
        <div class="acc-row">Designed for Multiple Platforms <span class="sign">+</span></div>
        <div class="acc-row">Great Support <span class="sign">+</span></div>
      </div>
    </div>
    <div class="col-right">
      <div class="col-title">TESTIMONIALS
        <div class="mini-pager">
          <span><svg width="8" height="10"><path d="M6 1 2 5l4 4" stroke="#fff" stroke-width="2" fill="none"/></svg></span>
          <span class="on"><svg width="8" height="10"><path d="M2 1l4 4-4 4" stroke="#fff" stroke-width="2" fill="none"/></svg></span>
        </div>
      </div>
      <div class="quote">
        <div class="avatar" role="img" aria-label="Portrait of the client"></div>
        <div class="who">Maren Holloway<small>Company Inc.</small></div>
        Lorem ipsum dolor sit amet, consectetur adipisicing elit, sed do eiusmod tempor incididunt ut labore et dolore magna aliqua. Curabitur pretium tincidunt lacus. Nulla gravida orci a odio. Nullam varius, turpis et commodo pharetra.
      </div>
    </div>
  </div>
</section>

<section class="cta" role="img" aria-label="Blurred photo background">
  <div class="cta-box">
    <h2>READY TO BUY OUR VOICEMAIL TO TEXT SERVICES?</h2>
    <span class="btn">BUY NOW!</span>
  </div>
</section>

<section class="partners">
  <div class="wrap">
    <h3>OUR PARTNERS</h3>
    <div class="partner-row">
      <div class="partner"><span></span></div>
      <div class="partner"><span></span></div>
      <div class="partner"><span></span></div>
      <div class="partner"><span></span></div>
      <div class="partner"><span></span></div>
    </div>
  </div>
</section>

<section class="tweetbar">
  <div class="wrap">
    <span class="dot"></span>
    <span>@hostnimbus Hostnimbus site totally down. Even the server status is also down t.co/Rk4wPlQs9f 50 Days ago</span>
    <div class="bullets"><span></span><span class="on"></span><span></span></div>
  </div>
</section>

<footer class="footer">
  <div class="wrap">
    <div>
      <div class="brand">KL9BQZ.io</div>
      <p>Welcome to Orchard theme developed for PressKit and ShopKit theme. So you can get two themes in one package. Also there is paid slider plugins too.</p>
    </div>
    <div>
      <h4>RECENT POSTS</h4>
      <ul class="posts">
        <li>Tunewell Audio with Post</li>
        <li>Stay ahead of the curve</li>
        <li>Getting Engaged</li>
        <li>Redesigning With Personality</li>
        <li>The Ride of Fireflies Haven</li>
      </ul>
    </div>
    <div>
      <h4>PHOTO STREAM</h4>
      <div class="stream" role="img" aria-label="Grid of recent photo thumbnails">
        <span></span><span></span><span></span><span></span><span></span><span></span><span></span><span></span><span></span>
      </div>
    </div>
    <div>
      <h4>TAGS</h4>
      <div class="tags">
        <span>Agency</span><span>Architecture</span><span>Illustration</span><span>Photography</span><span>Print</span><span>Technology</span><span>Web Design</span>
      </div>
    </div>
  </div>
</footer>

<footer class="copyright">
  <div class="wrap">Copyright 2014 KL9BQZ.io. All rights reserved.</div>
</footer>

</body>
</html>
```